Business card for communications

Need a business card for my consulting business - I work with not for profits, start ups and social enterprises on their media, communications campaigns.

Please see my website for colours, images and fonts www.morvenquillet.example

Morven Quillet
Communications & Campaign strategist
Sydney - Melbourne
M: 0498 317 250
E: morven@morvenquillet.example
S: morvenquillet
W: morvenquillet.example
T: @morvenquillet

(above is info only and can be presented any way e.g. should not have to be M for mobile - it should be an icon)
Updates

Dear designers I have updated the brief and uploaded high res images from my website for you to use. The designs so far with the use of images and icons are much better so far. Thank you I look forward to receiving your revised designs. Morven Quillet

Industry/Entity Type

Communications

Font styles to use
Sans Serif

Requirements
Must have
• Icons for contact details
Images from the website www.morvenquillet.example
Nice to have
• Images - attached

```html
<!DOCTYPE html>
<html lang="en">
<head>
<meta charset="utf-8">
<title>Morven Quillet – Business Card</title>
<link rel="stylesheet" href="https://fonts.googleapis.com/css2?family=Roboto:wght@300;400;700&family=Roboto+Condensed:wght@700&display=swap">
<style>
  :root {
    --backdrop: #7a7a7a;
    --card-front: #f7f7f5;
    --card-back: #e4e4e0;
    --accent: #f5cd0f;
    --ink: #222222;
    --ink-soft: #555555;
    --ink-muted: #8a8a8a;
  }
  * { box-sizing: border-box; margin: 0; padding: 0; }
  html, body {
    width: 1200px; height: 800px; overflow: hidden;
    background: var(--backdrop);
  }
  .canvas {
    position: relative; width: 1200px; height: 800px;
    font-family: "Roboto", Arial, sans-serif;
  }
  .card {
    position: absolute; top: 252px;
    width: 520px; height: 297px;
    box-shadow: 0 6px 18px rgba(0,0,0,0.25);
  }
  /* Back side */
  .card--back { left: 55px; background: var(--card-back); }
  .services {
    position: absolute; left: 40px; right: 40px; top: 112px;
    display: flex; justify-content: space-between; list-style: none;
  }
  .service {
    width: 100px; display: flex; flex-direction: column; align-items: center; gap: 8px;
  }
  .service__icon {
    width: 36px; height: 36px; border-radius: 6px;
    background: var(--accent); border: 2px solid var(--ink);
  }
  .service__label {
    font-family: "Roboto Condensed", "Arial Narrow", sans-serif;
    font-weight: 700; font-size: 9px; line-height: 1.1;
    letter-spacing: 0.04em; text-transform: uppercase;
    text-align: center; color: var(--ink);
  }
  /* Front side */
  .card--front { left: 625px; background: var(--card-front); }
  .card__band {
    position: absolute; top: 0; left: 0; right: 0; height: 13px;
    background: var(--accent);
  }
  .identity__name {
    position: absolute; top: 82px; left: 0; right: 0;
    text-align: center; font-weight: 300; font-size: 27px;
    letter-spacing: 0.06em; text-transform: uppercase; color: var(--ink);
  }
  .details {
    position: absolute; top: 140px; left: 0; right: 0;
    display: flex; align-items: center; justify-content: center; gap: 14px;
  }
  .role { text-align: right; }
  .role__title {
    font-weight: 700; font-size: 11px; line-height: 1.15;
    letter-spacing: 0.05em; text-transform: uppercase; color: var(--ink);
  }
  .role__location {
    font-size: 10px; letter-spacing: 0.08em; text-transform: uppercase;
    color: var(--ink-muted); margin-top: 1px;
  }
  .divider-plus { width: 16px; height: 16px; flex: none; }
  .contact { list-style: none; font-size: 10.5px; line-height: 1.3; color: var(--ink-soft); }
  .contact__item { display: flex; align-items: center; gap: 5px; height: 15px; }
  .contact__icon {
    width: 10px; height: 10px; flex: none;
    fill: none; stroke: var(--ink); stroke-width: 1.4;
    stroke-linecap: round; stroke-linejoin: round;
  }
  .contact__item--phone { font-weight: 700; font-size: 12px; letter-spacing: 0.04em; color: var(--ink); }
</style>
</head>
<body>
<main class="canvas">
  <section class="card card--back" aria-label="Card back: services">
    <ul class="services">
      <li class="service">
        <div class="service__icon" role="img" aria-label="Icon of a crossed pencil and ruler"></div>
        <span class="service__label">Communications<br>Strategy</span>
      </li>
      <li class="service">
        <div class="service__icon" role="img" aria-label="Icon of a typewriter"></div>
        <span class="service__label">Media<br>Relations</span>
      </li>
      <li class="service">
        <div class="service__icon" role="img" aria-label="Icon of stacked documents"></div>
        <span class="service__label">PR &amp;<br>Campaigns</span>
      </li>
      <li class="service">
        <div class="service__icon" role="img" aria-label="Icon of a light bulb"></div>
        <span class="service__label">Strategic<br>Counsel</span>
      </li>
    </ul>
  </section>

  <section class="card card--front" aria-label="Card front: contact details">
    <div class="card__band"></div>
    <h1 class="identity__name">Morven Quillet</h1>
    <div class="details">
      <div class="role">
        <p class="role__title">Communications &amp;<br>Campaign Strategist</p>
        <p class="role__location">Sydney - Melbourne</p>
      </div>
      <svg class="divider-plus" viewBox="0 0 16 16" aria-hidden="true">
        <rect x="6" y="0" width="4" height="16" fill="#222"/>
        <rect x="0" y="6" width="16" height="4" fill="#222"/>
      </svg>
      <ul class="contact">
        <li class="contact__item contact__item--phone">
          <svg class="contact__icon" viewBox="0 0 10 10" aria-label="Mobile"><rect x="2.5" y="0.8" width="5" height="8.4" rx="1"/><path d="M4.4 7.6h1.2"/></svg>
          0498 317 250
        </li>
        <li class="contact__item">
          <svg class="contact__icon" viewBox="0 0 10 10" aria-label="Email"><rect x="0.8" y="2" width="8.4" height="6" rx="0.6"/><path d="M1 2.4l4 3 4-3"/></svg>
          morven@morvenquillet.example
        </li>
        <li class="contact__item">
          <svg class="contact__icon" viewBox="0 0 10 10" aria-label="Video call"><rect x="0.8" y="2.6" width="5.6" height="4.8" rx="0.6"/><path d="M6.4 4.4l2.8-1.4v4l-2.8-1.4z"/></svg>
          morvenquillet
        </li>
        <li class="contact__item">
          <svg class="contact__icon" viewBox="0 0 10 10" aria-label="Website"><circle cx="5" cy="5" r="4.2"/><path d="M0.8 5h8.4M5 0.8c-2.2 2.4-2.2 6 0 8.4M5 0.8c2.2 2.4 2.2 6 0 8.4"/></svg>
          morvenquillet.example
        </li>
        <li class="contact__item">
          <svg class="contact__icon" viewBox="0 0 10 10" aria-label="Social handle"><path d="M1 1.5h8v5.2H4.2L2 8.6V6.7H1z"/></svg>
          @morvenquillet
        </li>
      </ul>
    </div>
  </section>
</main>
</body>
</html>
```